K.E.T.A. The Halbrook Grand Jury Testimony

This is the cover artwork for the audio version
of the re-creation of the Halbrook Grand Jury testimony based around the killing of Darnell Wexby. I need a cover for the library binders. I have the template for the binder that I can send. The title of the audio is: K.E.T.A. I would like the words Halbrook Grand Jury Testimony added in somehow with some creative graphics. I have a website with other audio covers. I also need the words: Unabridged CD format somewhere at the bottom. Can I send the binder template later?

Target Market(s)

Audiobook

Industry/Entity Type

Audio

Font styles to use
Serif

Requirements
Nice to have
• no bullets, no blood, no dead bodies, no police, no police cars, no protest, no
• violent images, no bullets
Should not have
• nice clear sleek look

```html
<!DOCTYPE html>
<html lang="en">
<head>
<meta charset="utf-8">
<title>K.E.T.A. — Halbrook Grand Jury Testimony</title>
<link rel="stylesheet" href="https://fonts.googleapis.com/css2?family=Tinos:ital,wght@0,400;0,700;1,400&display=swap">
<style>
  :root {
    --amber-light: #eeb27c;
    --amber-mid: #d9792f;
    --amber-deep: #b9501a;
    --brown-ink: #55302a;
    --frame-white: #ffffff;
    --rule-gold: #f4b72e;
  }
  html, body {
    margin: 0;
    padding: 0;
    width: 1200px;
    height: 1200px;
    overflow: hidden;
    background: var(--amber-deep);
  }
  .cover {
    display: block;
    width: 1200px;
    height: 1200px;
    font-family: "Tinos", "Times New Roman", serif;
  }
  .series-title { font-weight: 700; font-size: 110px; fill: var(--brown-ink); }
  .title-main { font-weight: 700; fill: var(--brown-ink); }
  .title-main.first { font-size: 124px; }
  .title-main.second { font-size: 112px; }
  .title-sub { font-weight: 400; font-size: 66px; fill: var(--brown-ink); }
  .title-initial { font-style: italic; font-weight: 400; font-size: 272px; fill: var(--frame-white); }
  .format-line { font-weight: 700; font-size: 24px; fill: var(--frame-white); }
</style>
</head>
<body>
<svg class="cover" viewBox="0 0 1200 1200" xmlns="http://www.w3.org/2000/svg">
  <defs>
    <radialGradient id="warm-glow" cx="0.55" cy="0.5" r="0.75">
      <stop offset="0" stop-color="var(--amber-light)"/>
      <stop offset="0.45" stop-color="var(--amber-mid)"/>
      <stop offset="1" stop-color="var(--amber-deep)"/>
    </radialGradient>
  </defs>

  <rect class="background" width="1200" height="1200" fill="url(#warm-glow)"
        role="img" aria-label="Weathered warm orange parchment texture"/>

  <rect class="frame" x="50" y="50" width="1100" height="1100" fill="none"
        stroke="var(--frame-white)" stroke-width="2.5"/>

  <text class="series-title" x="600" y="280" text-anchor="middle">K.E.T.A.</text>

  <g class="title-block">
    <text class="title-main first" x="256" y="568">HALBROOK</text>
    <text class="title-sub" x="442" y="632" textLength="538" lengthAdjust="spacing">Grand Jury</text>
    <text class="title-main second" x="368" y="736">ESTIMONY</text>
    <text class="title-initial" x="232" y="772">T</text>
  </g>

  <line class="gold-rule" x1="478" y1="1046" x2="746" y2="1046" stroke="var(--rule-gold)" stroke-width="3"/>

  <text class="format-line" x="322" y="1102" textLength="558" lengthAdjust="spacing">Unabridged  CD  format</text>
</svg>
</body>
</html>
```